Laminated Training Card; highly professional yet engaging, colorful, fits branding

We need an 8 1/2" x 11" piece, printed front and back, to inspire and offer instructions for nonprofit leaders on key coaching skills to use with their staff. Though it's in a professional services setting, this piece communicates a sense of fun and excitement to encourage leaders to try out these skills, and keep the training card close at hand. An infographic style would be ideal.

Target Market(s)

Nonprofit leaders will use the laminated training card in a face to face training class, and then take it back to the office to use to 'train' their staff

Industry/Entity Type

Training

Font styles to use
Serif

Requirements
Must have
• See project brief attached
Nice to have
Should not have

```html
<!DOCTYPE html>
<html lang="en">
<head>
<meta charset="utf-8">
<title>Accountability Culture Training Card</title>
<link href="https://fonts.googleapis.com/css2?family=Libre+Baskerville:ital,wght@0,400;1,400&family=Open+Sans:ital,wght@0,400;0,600;1,400&display=swap" rel="stylesheet">
<style>
  :root {
    --orange: #e8562a;
    --lime: #b3c237;
    --ink: #2b2b2b;
    --grey: #555555;
    --brown: #6b4a36;
    --page-edge: #dddddd;
    --paper: #ffffff;
  }
  * { margin: 0; padding: 0; box-sizing: border-box; }
  html, body { width: 1200px; height: 1200px; overflow: hidden; background: var(--paper); }
  body { position: relative; font-family: "Open Sans", Arial, sans-serif; color: var(--ink); }

  .sheet {
    position: absolute; top: 248px; width: 547px; height: 704px;
    background: var(--paper); border: 1px solid var(--page-edge);
  }
  .sheet--front { left: 46px; }
  .sheet--back { left: 618px; }
  .sheet > * { position: absolute; }

  .art { border-radius: 6px; }

  .brand { display: flex; align-items: center; gap: 6px; }
  .brand__dot { width: 26px; height: 26px; border-radius: 50%; background: var(--brown); }
  .brand__name {
    font-family: "Libre Baskerville", Georgia, serif; color: var(--brown);
    font-size: 14px; line-height: 1.2;
  }

  .card-kicker {
    left: 0; width: 100%; text-align: center;
    font-family: "Libre Baskerville", Georgia, serif; font-size: 11.5px; color: var(--grey);
    letter-spacing: 0.2px;
  }
  .card-title {
    left: 0; width: 100%; text-align: center;
    font-family: "Libre Baskerville", Georgia, serif; font-size: 19px; font-weight: 400; color: var(--ink);
  }
  .card-title__accent { color: var(--lime); }
  .title-rule { height: 2px; background: var(--lime); }

  .section-head {
    font-family: "Libre Baskerville", Georgia, serif; font-size: 14px; font-weight: 400; color: var(--orange);
    white-space: nowrap;
  }
  .section-head span { text-decoration: underline; text-underline-offset: 3px; }

  .copy { font-size: 9.6px; line-height: 12.2px; }
  .copy p + p { margin-top: 12px; }
  .copy--tight p + p { margin-top: 0; }

  .brag-quotes { font-family: "Libre Baskerville", Georgia, serif; font-style: italic; font-size: 9px; line-height: 12px; color: var(--lime); }

  .results-head {
    font-family: "Libre Baskerville", Georgia, serif; font-size: 13px; font-weight: 400; line-height: 16px;
    color: var(--orange); text-align: center; white-space: nowrap;
  }
  .results-rule { height: 1.5px; background: var(--orange); }
  .results-list { list-style: none; text-align: center; font-size: 10px; line-height: 13px; }
  .results-list li { display: flex; justify-content: center; align-items: center; gap: 4px; }

  .sources { font-size: 8px; line-height: 12px; }
  .sources h3 { font-size: 10px; font-weight: 600; margin-bottom: 2px; }
  .sources li { list-style: none; }

  .contact { font-size: 8px; line-height: 11px; font-style: italic; }
  .contact .brand__dot { width: 18px; height: 18px; }
  .contact .brand__name { font-size: 11px; }

  .site-url { left: 0; width: 100%; text-align: center; font-size: 9.6px; letter-spacing: 0.3px; }
</style>
</head>
<body>

<section class="sheet sheet--front">
  <div class="brand" style="left:182px; top:32px;">
    <div class="brand__dot"></div>
    <div class="brand__name">Northpath Center<br><span style="font-size:11px;">for Nonprofit Leadership</span></div>
  </div>

  <p class="card-kicker" style="top:76px;">CREATE AN ACCOUNTABILITY CULTURE WITH TEAMS AND ALLIES</p>
  <h1 class="card-title" style="top:92px;">VALUABLE TIPS FOR <span class="card-title__accent">SUCCESS</span></h1>
  <div class="title-rule" style="left:128px; top:118px; width:290px;"></div>

  <div class="art" role="img" aria-label="Illustration of a thoughtful businessman with a question mark" style="left:446px; top:108px; width:82px; height:178px; background:linear-gradient(180deg,#e9e2d6,#f3b08f);"></div>

  <h2 class="section-head" style="left:31px; top:138px;"><span>Powerful Questions</span></h2>
  <div class="copy" style="left:31px; top:170px; width:410px;">
    <p>Coach yourself asking powerful questions; they break your internal monologue.<br>Ask others a powerful question — that you don’t answer.&nbsp; They will feel deeply heard.</p>
    <p>Dream one moment: What’s possible? And establish accountability the next:<br>What should I do when you miss your deadline?</p>
    <p>Asking questions isn’t reserved for the leader.<br>Whoever asks the powerful questions is the leader in the moment.</p>
    <p>With whom is it safe to ask powerful questions in your culture?</p>
  </div>

  <div class="art" role="img" aria-label="Illustration of a school of orange fish following one blue fish" style="left:30px; top:310px; width:180px; height:172px; background:radial-gradient(ellipse at 45% 50%,#f6a03a 0%,#fbd3a0 60%,#ffffff 100%);"></div>

  <h2 class="section-head" style="right:33px; top:304px;">4 Dimensions of <span>Leadership</span></h2>
  <div class="copy copy--tight" style="left:249px; top:336px; width:270px;">
    <p>Knowing when to move between these stances =<br>leadership mastery.</p>
    <p style="margin-top:12px;">Leading from the front: eyes on the vision and staying connected to those who follow</p>
    <p>Leading from the side:&nbsp; locking arms in the company of equals. Eyes on the shared vision, but each has their own path to get there.</p>
    <p>Leading from behind: ‘fading’ while still holding the space. You’ve got their backs.</p>
    <p>Leading from above: seeing the big picture</p>
  </div>

  <h2 class="section-head" style="left:31px; top:482px;">4 <span>Team Toxins</span></h2>
  <div class="copy" style="left:31px; top:512px; width:320px;">
    <p>Defensiveness, blaming, stonewalling and contempt. We all do it, especially when stress is high. There’s camaraderie through complaining. But left unchecked, great work comes to a halt.</p>
    <p>Antidotes:<br>-&nbsp; Ask: what are you defending? What am I protecting? How can we keep this from spreading?<br>-&nbsp; Toxins can flood us. Take a break and come back to the conversation.<br>-&nbsp; Check assumptions. ‘I assume you have money in your budget. I assume you don’t want to be involved. I assume you’re supporting me on this.</p>
  </div>

  <div class="art" role="img" aria-label="Illustration of a businessman opening his shirt like a superhero, with orange burst lines" style="left:354px; top:480px; width:168px; height:166px; background:radial-gradient(circle at 50% 55%,#ffffff 0%,#fde1c8 55%,#f7a65c 100%);"></div>

  <p class="site-url" style="top:662px;">www.northpathcenter.org</p>
</section>

<section class="sheet sheet--back">
  <h2 class="section-head" style="left:31px; top:30px;"><span>Brag Bites</span></h2>

  <div class="art" role="img" aria-label="Illustration of two businessmen shaking hands and giving a thumbs up" style="left:34px; top:54px; width:208px; height:160px; background:linear-gradient(135deg,#f0ddd0,#4a3a3a);"></div>

  <div class="copy" style="left:250px; top:66px; width:262px; font-size:9.4px;">
    <p>Brag on the team. Stay away from generalizations; ‘I have a great team’.&nbsp; Instead name a value you honored, an obstacle overcome, or what others count on. Have 10 team brag bites in your brag bag ready at all times.</p>
  </div>
  <div class="brag-quotes" style="left:250px; top:127px; width:262px;">
    <p>‘We fell short of the goal. But we never gave up.’</p>
    <p>‘We didn’t expect the new people to step up so quickly.</p>
    <p>We set aside egos and followed whoever had the best idea.’</p>
    <p>‘The whole organization counted on our team’s optimism and hopefulness.’</p>
  </div>

  <h2 class="section-head" style="right:33px; top:210px;"><span>Team Charter</span></h2>

  <div class="art" role="img" aria-label="Illustration of colorful hands joined in a circle" style="left:378px; top:236px; width:136px; height:132px; border-radius:50%; background:conic-gradient(#6ec5e6,#f7c62f,#8dc63f,#e8562a,#6ec5e6);"></div>

  <div class="copy" style="left:30px; top:258px; width:330px; font-size:9.4px;">
    <p>Teams don’t find their focus from the mission statement. It’s too broad, vague and doesn’t answer the question: What is our team’s unique contribution to achieving the mission? Your&nbsp; answer is your Team Charter. Name your values, what’s your impact, how you celebrate success, even what you do when things go wrong.</p>
    <p>The Charters answers the questions: if we weren’t here, what would be missing? What do we want people to count on from us?</p>
  </div>

  <div class="art" role="img" aria-label="Illustration of a person meditating on a cloud with a thought bubble" style="left:28px; top:362px; width:142px; height:170px; background:linear-gradient(180deg,#cfe9f7,#9fd3ef);"></div>

  <h2 class="section-head" style="left:209px; top:388px;"><span>Mindfulness</span></h2>
  <div class="copy" style="left:209px; top:416px; width:306px; font-size:9.6px;">
    <p>Whatever gets your attention gets YOU. Become the director of your attention. Mindfulness strengthens your attention muscles</p>
  </div>

  <h2 class="results-head" style="left:160px; top:456px; width:300px;">ACCOUNTABILITY CULTURES<br>DELIVER RESULTS</h2>
  <div class="results-rule" style="left:213px; top:496px; width:194px;"></div>
  <ul class="results-list" style="left:190px; top:504px; width:240px;">
    <li><svg width="9" height="9" viewBox="0 0 10 10"><rect x="0.5" y="0.5" width="9" height="9" fill="none" stroke="#2b2b2b"/><path d="M2 5 L4.2 7.2 L8 2.5" fill="none" stroke="#2b2b2b" stroke-width="1.2"/></svg>Improve productivity</li>
    <li><svg width="9" height="9" viewBox="0 0 10 10"><rect x="0.5" y="0.5" width="9" height="9" fill="none" stroke="#2b2b2b"/><path d="M2 5 L4.2 7.2 L8 2.5" fill="none" stroke="#2b2b2b" stroke-width="1.2"/></svg>Speed decision making</li>
    <li><svg width="9" height="9" viewBox="0 0 10 10"><rect x="0.5" y="0.5" width="9" height="9" fill="none" stroke="#2b2b2b"/><path d="M2 5 L4.2 7.2 L8 2.5" fill="none" stroke="#2b2b2b" stroke-width="1.2"/></svg>Reduce stress and compassion fatigue</li>
    <li><svg width="9" height="9" viewBox="0 0 10 10"><rect x="0.5" y="0.5" width="9" height="9" fill="none" stroke="#2b2b2b"/><path d="M2 5 L4.2 7.2 L8 2.5" fill="none" stroke="#2b2b2b" stroke-width="1.2"/></svg>Have more fun and fulfillment</li>
    <li><svg width="9" height="9" viewBox="0 0 10 10"><rect x="0.5" y="0.5" width="9" height="9" fill="none" stroke="#2b2b2b"/><path d="M2 5 L4.2 7.2 L8 2.5" fill="none" stroke="#2b2b2b" stroke-width="1.2"/></svg>Build trust</li>
  </ul>

  <div class="sources" style="left:31px; top:592px; width:240px;">
    <h3>SOURCES</h3>
    <ul>
      <li>-&nbsp; ‘Bragging Well at Work’ by<br>&nbsp;&nbsp;&nbsp;Dana Welles</li>
      <li>-&nbsp; Rising Together by (need to fill this in)</li>
      <li>-&nbsp; Coaching Practice Institute (CPI): 4-Dimensional<br>&nbsp;&nbsp;&nbsp;Leadership Model</li>
      <li>-&nbsp; Levels of Focus: Martin Hale &amp; CPI</li>
    </ul>
  </div>

  <div class="contact" style="left:354px; top:590px; width:170px;">
    <div class="brand" style="font-style:normal; margin-bottom:3px;">
      <div class="brand__dot"></div>
      <div class="brand__name">Northpath Center<br><span style="font-size:8px;">for Nonprofit Leadership</span></div>
    </div>
    <p>48 Alder Lane, Suite 210<br>Riverton, GA 30999<br>www.northpathcenter.org<br>555-014-2290<br>info@northpathcenter.org<br>501(c)(3) organization funded by donations</p>
  </div>
</section>

</body>
</html>
```